Brochure Design Project (Design Studio)

Items required:
1-Brochure. We suggest 15Cm X 15 Cm after cutting.
2-Business Card.
3-Head letter.
4-Folder ( folder should carry the Brochure in pocket and the business card in a pocket on the opposite side of the folder.
5-Envelope to carry everything.
This brochure is expected to draw attention of high level management in companies to the quality and creativity of the design work and encourage them to do business with us. note that brochure will be printed in high quality printing and paper.
The game plan is as follows:
Over all description, the theme of the brochure is drawn from the website theme (website will be uploaded shortly, pictures of the website are attached, logo appears in the top left corner). Please avoid direct copying from the website unless it is a creative copying, just draw the theme from there. however, we need it to be elegant, stylish and class in colors and style. This is a MUST.
Furthermore, the main items of the Brochure:
1-The Studio is not just a studio: we will take about how Branding. A file is attached of the content. (slight changes/modification can apply during the designing process)
2-The Process: this one has to be a visual illustration of the process, it has to be very creative, could be elegant arrows and comics, could be elegant drawing, could be an elegant icons. The drawing should be separate from the steps, we need to the drawing and we need to have the steps listed and commentary, or if want to integrate both in one in an artistic way. Just don’t lose track of the theme and elegance. (steps and commentary are attached, slight changes/modification can apply at anytime.
3-Our Team: another drawing of your suggestion to illustrate the team members, we need to include the names and designation as well leave a place for some of them to say what they need to say about their style of designing. I leave it for your imagination to put this all together in a nice attractive visual illustration.
4-Works: this section will generally show the works of our designers. It needs to be focused on the works themselves, client should be able to view the details of the works ( note that when it comes to brochures and websites, we don’t need to reach to the extent with which the client can read the text in those pictures of the website or brochure, but still can see the overall design clearly). Each design is to carry the name of the designer. Last thing, this section will classify works into categories, like, Brochures, Corporate identity, print design. We didn’t finalize those categories, we will provide them to you shortly, last thing to be said, we are planning to include around 25-30 designs of each sub-category, eg. Corporate identity will have 30 business card s designs and 30 stationary designs.
5-Contacts: the company contacts.
We the brochure after printing should be 15x15 Cm.
Creativity and art work is a major player in selection.
general managers, owners
Printing

```html
<!DOCTYPE html>
<html lang="en">
<head>
<meta charset="utf-8">
<title>Solvane Studio – Brochure 15 x 15 cm</title>
<link rel="stylesheet" href="https://fonts.googleapis.com/css2?family=Roboto:wght@300;400;500;700&family=Roboto+Condensed:wght@300;400&display=swap">
<style>
  :root{
    --board-top:#9aa3a5;
    --board-mid:#d5dadb;
    --board-bottom:#e4e7e8;
    --ink:#0b0b0b;
    --ink-soft:#161616;
    --grey-band:#5f5f5f;
    --grey-band-dark:#3a3a3a;
    --text-light:#c9c9c9;
    --text-mid:#9a9a9a;
    --text-dim:#5d5d5d;
    --rule:#3a3a3a;
    --accent:#d4161c;
    --label-grey:#7a7f80;
  }
  *{box-sizing:border-box;margin:0;padding:0}
  html,body{width:1200px;height:1200px;overflow:hidden}
  body{
    position:relative;
    background:linear-gradient(180deg,var(--board-top) 0%,var(--board-mid) 45%,var(--board-bottom) 100%);
    font-family:"Roboto",Arial,sans-serif;
  }

  /* ---------- panels ---------- */
  .panel{position:absolute;top:56px;width:527px;height:526px;background:var(--ink);overflow:hidden}
  .panel--front{left:52px}
  .panel--back{left:623px;display:flex}

  .panel-label{position:absolute;top:632px;font:500 23px/1 "Roboto",Arial,sans-serif;color:var(--ink-soft)}
  .panel-label::first-letter{color:var(--accent)}
  .panel-label--front{left:68px}
  .panel-label--back{left:643px}

  /* ---------- front ---------- */
  .studio-mark{position:absolute;top:76px;left:0;width:100%;text-align:center;white-space:nowrap}
  .studio-mark__name{font:400 19px/1 "Roboto",Arial,sans-serif;color:var(--accent);letter-spacing:.5px}
  .studio-mark__divider{display:inline-block;width:1px;height:14px;background:var(--text-mid);margin:0 8px;vertical-align:-1px}
  .studio-mark__tagline{font:300 11px/1 "Roboto Condensed",Arial,sans-serif;color:var(--text-mid);letter-spacing:2.4px}

  .hero{position:absolute;top:228px;left:0;width:100%;text-align:center}
  .hero__lead{font:300 21px/26px "Roboto",Arial,sans-serif;color:var(--text-light)}
  .hero__title{font:500 28px/30px "Roboto",Arial,sans-serif;color:#e2e2e2;letter-spacing:.5px}
  .hero__sub{position:absolute;top:67px;left:0;width:100%;font:300 9.5px/12px "Roboto",Arial,sans-serif;color:var(--text-dim)}

  .strip-rule{position:absolute;left:0;right:0;top:383px;border-top:1px dotted var(--rule)}
  .thumb-strip{position:absolute;left:0;top:389px;width:100%;height:52px;display:flex}
  .thumb{height:100%}
  .thumb--1{width:82px;background:linear-gradient(135deg,#f1d6da,#d9c7c9 60%,#8d8d8d)}
  .thumb--2{width:72px;background:linear-gradient(90deg,#e7e5e0,#6f6a64 45%,#1e1c1b)}
  .thumb--3{width:72px;background:linear-gradient(120deg,#2a2a2a,#d8d8d8 45%,#8e1a1d 60%,#222)}
  .thumb--4{width:68px;background:linear-gradient(160deg,#f4f4f4,#b43c45 45%,#4c4c4c);outline:2px solid #a7c84a;outline-offset:-2px}
  .thumb--5{width:86px;background:linear-gradient(135deg,#f2ede2,#d9b073 45%,#3a3a3a)}
  .thumb--6{width:76px;background:linear-gradient(90deg,#f3f3f3,#b75a5a 40%,#6b6b6b 70%,#efefef)}
  .thumb--7{width:71px;background:linear-gradient(135deg,#d9d9d9,#1b1b1b 40%,#0b0b0b)}
  .strip-base{position:absolute;left:0;right:0;top:441px;border-top:1px solid var(--rule)}

  .services{position:absolute;top:460px;left:0;width:100%;text-align:center;font:300 12px/14px "Roboto Condensed",Arial,sans-serif;color:var(--text-mid)}
  .services span{margin:0 5px}
  .contact-line{position:absolute;top:499px;left:0;width:100%;text-align:center;font:300 7.5px/10px "Roboto Condensed",Arial,sans-serif;color:var(--text-mid)}
  .contact-line span{margin:0 4px}

  /* ---------- back ---------- */
  .work-grid{width:215px;height:100%;display:flex;flex-direction:column;flex:none}
  .work-row{display:flex}
  .work-row--1{height:75px}.work-row--2{height:91px}.work-row--3{height:102px}
  .work-row--4{height:87px}.work-row--5{height:83px}.work-row--6{height:88px}
  .work{height:100%}
  .work--pencils{width:114px;background:linear-gradient(150deg,#e6c23a,#3a9bd4 35%,#d9462f 60%,#4fa64b)}
  .work--pyramid{width:101px;background:linear-gradient(160deg,#e8e2dc,#5b3a2d 55%,#2a1b15)}
  .work--box{width:94px;background:linear-gradient(135deg,#f1f1f1,#1f2a5a 45%,#2a2a2a)}
  .work--book{width:121px;background:linear-gradient(140deg,#d9d9d9,#1b1b1b 40%,#2b2b2b)}
  .work--spread{width:144px;background:linear-gradient(120deg,#101010,#e7e3dc 35%,#c8c0b3 70%,#3a2b22)}
  .work--cutout{width:71px;background:linear-gradient(160deg,#f5f5f5,#111 55%,#f0f0f0)}
  .work--folders{width:88px;background:linear-gradient(135deg,#f2f2f2,#e73a8a 35%,#f0d52a 55%,#3a9bd4 75%,#8acd3a)}
  .work--cover{width:127px;background:linear-gradient(135deg,#1a1a1a,#bfc3c6 45%,#111)}
  .work--bulb{width:88px;background:radial-gradient(circle at 50% 40%,#8c8c8c,#101010 60%)}
  .work--red{width:127px;background:linear-gradient(150deg,#ececec,#d5121a 35%,#b20d14)}
  .work--green{width:88px;background:radial-gradient(circle at 50% 50%,#8fd64a,#2b2b2b 55%,#c9a56a)}
  .work--fan{width:127px;background:linear-gradient(135deg,#d9d9d9,#1f6fb0 40%,#c0262c 65%,#e8e8e8)}

  .side-band{width:32px;height:100%;flex:none;background:linear-gradient(90deg,var(--grey-band) 0 22px,var(--grey-band-dark) 22px)}

  .copy{position:relative;flex:1;color:var(--text-mid);font:300 10.4px/12px "Roboto",Arial,sans-serif}
  .copy > *{position:absolute;left:13px;right:15px}
  .copy__title{top:19px;font:500 12px/14px "Roboto",Arial,sans-serif;color:var(--text-light);letter-spacing:.4px;padding-bottom:5px;border-bottom:1px dotted var(--rule)}
  .copy__para{text-align:justify}
  .copy__para--1{top:52px}
  .copy__para--2{top:124px}
  .copy__para--3{top:172px}
  .dropcap{color:var(--accent);font-weight:500;font-size:13px}
  .copy__heading--1{top:294px}
  .copy__list--1{top:313px}
  .copy__heading--2{top:372px}
  .copy__list--2{top:392px}
  .copy__list{list-style:none;padding-left:44px;counter-reset:n}
  .copy__list li{counter-increment:n;position:relative}
  .copy__list li::before{content:counter(n) ".";position:absolute;left:-16px}
  .copy__footer{top:496px;border-top:1px dotted var(--rule);padding-top:10px;text-align:right;font-size:8.5px;line-height:10px}
  .copy__footer strong{font-weight:400;color:var(--text-light)}

  /* ---------- board notes ---------- */
  .spec{position:absolute;left:50px;top:1003px;font:300 23px/26px "Roboto",Arial,sans-serif;color:var(--label-grey)}
  .board-mark{position:absolute;left:50px;top:1110px;white-space:nowrap}
  .board-mark__name{font:400 34px/1 "Roboto",Arial,sans-serif;color:var(--accent)}
  .board-mark__divider{display:inline-block;width:2px;height:26px;background:#555;margin:0 12px;vertical-align:-3px}
  .board-mark__tagline{font:300 20px/1 "Roboto Condensed",Arial,sans-serif;color:#555;letter-spacing:4px}
</style>
</head>
<body>

<section class="panel panel--front" aria-label="Brochure front">
  <div class="studio-mark">
    <span class="studio-mark__name">Solvane Studio</span><span class="studio-mark__divider"></span><span class="studio-mark__tagline">CREATIVE WORKS</span>
  </div>

  <div class="hero">
    <p class="hero__lead">Perosnify your</p>
    <h1 class="hero__title">BUSINESS</h1>
    <p class="hero__sub">We are more than just a creative studio;<br>we can personify your business and dress to impress!</p>
  </div>

  <div class="strip-rule"></div>
  <div class="thumb-strip">
    <div class="thumb thumb--1" role="img" aria-label="Photo of a pink stationery design"></div>
    <div class="thumb thumb--2" role="img" aria-label="Photo of an open printed book"></div>
    <div class="thumb thumb--3" role="img" aria-label="Photo of a black and red CD package"></div>
    <div class="thumb thumb--4" role="img" aria-label="Screenshot of a website design"></div>
    <div class="thumb thumb--5" role="img" aria-label="Photo of corporate identity cards"></div>
    <div class="thumb thumb--6" role="img" aria-label="Photo of a folded patterned leaflet"></div>
    <div class="thumb thumb--7" role="img" aria-label="Photo of a black brochure cover"></div>
  </div>
  <div class="strip-base"></div>

  <p class="services"><span>Graphic Design</span>|<span>Corporate Identity</span>|<span>Print Design</span>|<span>Web Design</span></p>
  <p class="contact-line"><span>Tel 00 000 2 555 0142</span>|<span>Fax 00 000 2 555 0143</span>|<span>P.O. Box 10452, Harbour City</span>|<span>Web: www.solvanestudio.com</span></p>
</section>
<p class="panel-label panel-label--front">Front</p>

<section class="panel panel--back" aria-label="Brochure back">
  <div class="work-grid">
    <div class="work-row work-row--1">
      <div class="work work--pencils" role="img" aria-label="Photo of coloured pencils"></div>
      <div class="work work--pyramid" role="img" aria-label="Photo of pyramid packaging with coffee beans"></div>
    </div>
    <div class="work-row work-row--2">
      <div class="work work--box" role="img" aria-label="Photo of a product box design"></div>
      <div class="work work--book" role="img" aria-label="Photo of a black hardcover book"></div>
    </div>
    <div class="work-row work-row--3">
      <div class="work work--spread" role="img" aria-label="Photo of an open catalogue spread"></div>
      <div class="work work--cutout" role="img" aria-label="Photo of a black cut-out card"></div>
    </div>
    <div class="work-row work-row--4">
      <div class="work work--folders" role="img" aria-label="Photo of colourful folders"></div>
      <div class="work work--cover" role="img" aria-label="Photo of a silver brochure cover"></div>
    </div>
    <div class="work-row work-row--5">
      <div class="work work--bulb" role="img" aria-label="Poster with a light bulb"></div>
      <div class="work work--red" role="img" aria-label="Photo of a red brochure"></div>
    </div>
    <div class="work-row work-row--6">
      <div class="work work--green" role="img" aria-label="Photo of a greeting card with a green circle"></div>
      <div class="work work--fan" role="img" aria-label="Photo of fanned printed leaflets"></div>
    </div>
  </div>

  <div class="side-band"></div>

  <article class="copy">
    <h2 class="copy__title">BRANDING</h2>
    <p class="copy__para copy__para--1"><span class="dropcap">D</span>o you prefer to work with specific Individuals over others? Do you feel that working with those individuals give you the peace of mind because you know that they are Enthusiastic, ethical, Goal Focused, Committed, Disciplined, creative, visionary and self-aware?</p>
    <p class="copy__para copy__para--2">Well, probably you like to work with companies of the same qualities as those persons! COMPANIES HAVE PERSONALITIES TOO.</p>
    <p class="copy__para copy__para--3">Branding is your vehicle to deliver the traits of your company to the audience. Branding assist you to control the perception of company among public.<br>If you are very organized company, deliver on time, committed to your clients, produce quality products to the highest standards. Branding is the key to make the public hear and believe those qualities and consider your products as their 1st choice.</p>

    <p class="copy__heading copy__heading--1">Strong Branding Means you company is:</p>
    <ol class="copy__list copy__list--1">
      <li>Large and established.</li>
      <li>A synonym of Quality.</li>
      <li>Experienced and reliable.</li>
    </ol>

    <p class="copy__heading copy__heading--2">Branding gives you:</p>
    <ol class="copy__list copy__list--2">
      <li>Loyalty and advocacy.</li>
      <li>Influence of choice.</li>
      <li>Command a price premium.</li>
      <li>Uniqueness.</li>
      <li>Growth of your business and products.</li>
    </ol>

    <p class="copy__footer">Contact Us: <strong>00 000 2 555 0142</strong></p>
  </article>
</section>
<p class="panel-label panel-label--back">Back</p>

<p class="spec">Brochure<br>15 x 15 cm</p>

<div class="board-mark">
  <span class="board-mark__name">Solvane Studio</span><span class="board-mark__divider"></span><span class="board-mark__tagline">CREATIVE WORKS</span>
</div>

</body>
</html>
```